Basin And Slab Inc. Cultured marble and solidsurface fabrication and installation builders and home

We need a postcard design for a cultured marble company in Wills Point Texas. We manufacture showers, shower pans, bath tubs, vanity sinks and solid surface kitchen counter tops. Company name is Basin and Slab Inc. We are looking to generate sales and inform customers of what we offer. We are open to the public as well as home builders and offer standard and custom applications. New construction and remodels.

Target Market(s)

Home builders and home owners

Industry/Entity Type

Construction

Font styles to use
Serif
Sans Serif
Script

Colors
000000
85acd3
0555a3
3176b5
0692cd
33a6d7
85cae6
d0dfed

Requirements
Must have
• Name, services offered

```html
<!DOCTYPE html>
<html lang="en">
<head>
<meta charset="utf-8">
<title>Basin And Slab Inc. – Postcard</title>
<link href="https://fonts.googleapis.com/css2?family=Roboto+Slab:wght@700;800&family=Open+Sans:wght@400;600;700;800&display=swap" rel="stylesheet">
<style>
:root{
  --black:#000000;
  --ink:#141414;
  --charcoal:#2a2a2a;
  --steel:#85acd3;
  --navy:#0555a3;
  --blue:#3176b5;
  --sky:#0692cd;
  --aqua:#33a6d7;
  --ice:#85cae6;
  --mist:#d0dfed;
  --white:#ffffff;
  --backdrop:#e9edf1;
}
*{margin:0;padding:0;box-sizing:border-box}
html,body{width:796px;height:1200px;overflow:hidden}
body{background:var(--backdrop);font-family:"Open Sans",Arial,sans-serif;position:relative}
.card{position:absolute;left:50px;width:696px;height:530px;overflow:hidden;box-shadow:0 4px 14px rgba(0,0,0,.25)}
.card svg.art{position:absolute;inset:0;width:100%;height:100%}
.abs{position:absolute}

/* front */
.front{top:40px;background:linear-gradient(135deg,var(--charcoal),var(--ink) 60%,var(--black))}
.hours-label{left:20px;top:34px;color:var(--aqua);font-weight:800;font-size:15px;white-space:nowrap}
.hours-days{left:192px;top:14px;color:var(--white);font-weight:700;font-size:13px;white-space:nowrap}
.hours-time{left:188px;top:30px;color:var(--aqua);font-weight:800;font-size:28px;line-height:1;white-space:nowrap}
.brand{right:20px;top:10px;text-align:right;font-family:"Roboto Slab",Georgia,serif;line-height:1.2;white-space:nowrap}
.brand-name{color:var(--white);font-size:29px;font-weight:800}
.brand-line1{color:var(--ice);font-size:26px;font-weight:700;background:rgba(5,85,163,.35);padding:0 6px}
.brand-line2{color:var(--white);font-size:24px;font-weight:700}
.showcase{left:20px;top:112px;width:300px;height:210px;background:linear-gradient(90deg,#9aa3aa,#d8d2c6 50%,#c9b79a);border:3px solid var(--white)}
.showcase span{position:absolute;top:8px;color:var(--white);font-size:15px;font-weight:600;text-shadow:0 1px 2px rgba(0,0,0,.6)}
.offer-title{left:420px;top:180px;color:var(--white);font-weight:800;font-size:34px}
.offer-list{left:470px;top:238px;list-style:none;color:var(--ink);font-weight:700;font-size:15px;line-height:1.4}
.offer-list li{position:relative;padding-left:16px}
.offer-list li::before{content:"";position:absolute;left:0;top:7px;width:8px;height:8px;border-radius:50%;background:var(--sky)}
.badge{left:300px;top:352px;width:150px;height:150px;border-radius:50%;background:var(--sky);border:5px solid var(--white);box-shadow:0 0 0 3px var(--navy);color:var(--white);text-align:center;display:flex;flex-direction:column;justify-content:center;font-weight:800;line-height:1.05}
.badge .big{font-size:25px}
.badge .small{font-size:11px;margin-top:4px}
.contact{list-style:none;color:var(--white);font-size:15px;line-height:1.3}
.contact li{display:flex;align-items:flex-start;gap:8px;margin-bottom:5px}
.contact svg{width:15px;height:15px;flex:none;margin-top:2px}
.front .contact{left:30px;top:350px}

/* back */
.back{top:620px;background:var(--white)}
.round-photo{left:162px;top:24px;width:116px;height:116px;border-radius:50%;background:radial-gradient(circle at 45% 40%,#e8e6e1,#9eb4c6 70%);border:4px solid var(--white)}
.about-title{left:0;top:190px;width:190px;height:32px;background:var(--black);color:var(--white);font-weight:800;font-size:18px;padding:3px 0 0 22px}
.about-text{left:20px;top:228px;width:310px;font-size:11.5px;line-height:1.3;color:var(--ink)}
.about-text p+p{margin-top:8px}
.call{left:20px;top:400px;color:var(--sky);font-weight:800;font-size:24px;line-height:1.2}
.back .contact{left:22px;top:438px;color:var(--ink);font-size:12px;line-height:1.2}
.back .contact li{margin-bottom:2px}
.back .contact svg{width:12px;height:12px;margin-top:1px}
.stamp{right:26px;top:28px;width:70px;height:82px;border:2px solid #9a9a9a}
</style>
</head>
<body>

<section class="card front" aria-label="Postcard front">
  <svg class="art" viewBox="0 0 696 530" aria-hidden="true">
    <path d="M300 530 C330 330 420 220 696 150 L696 530 Z" fill="var(--white)"/>
    <path d="M250 530 C300 300 430 190 696 128 L696 150 C430 215 330 320 300 530 Z" fill="var(--sky)"/>
    <path d="M0 330 C160 360 260 300 330 230 C300 320 220 380 0 360 Z" fill="var(--aqua)" opacity=".85"/>
    <polygon points="438,170 696,170 696,228 408,228" fill="var(--sky)"/>
  </svg>
  <div class="abs hours-label">OFFICE/SHOWROOM:</div>
  <div class="abs hours-days">Monday-Friday</div>
  <div class="abs hours-time">8:00-4:30</div>
  <div class="abs brand">
    <div class="brand-name">BASIN AND SLAB INC</div>
    <div class="brand-line1">CULTERED MARBLE</div>
    <div class="brand-line2">AND SOLID SURFACE</div>
  </div>
  <div class="abs showcase" role="img" aria-label="Before and after photo of a remodeled shower and bathroom">
    <span style="left:60px">Before</span><span style="left:170px">After</span>
  </div>
  <div class="abs offer-title">WE OFFER</div>
  <ul class="abs offer-list">
    <li>Shower pans</li>
    <li>Shower and tub<br>enclosures</li>
    <li>Vanity tops</li>
    <li>Bath tubs</li>
    <li>Solid Surface Kitchen<br>and bath counter tops</li>
  </ul>
  <div class="abs badge"><span class="big">CUSTOM</span><span class="big">HOMES</span><span class="small">AND REMODELS</span></div>
  <ul class="abs contact">
    <li><svg viewBox="0 0 24 24"><path fill="currentColor" d="M6.6 10.8a15 15 0 0 0 6.6 6.6l2.2-2.2a1 1 0 0 1 1-.25 11.4 11.4 0 0 0 3.6.57 1 1 0 0 1 1 1V20a1 1 0 0 1-1 1A17 17 0 0 1 3 4a1 1 0 0 1 1-1h3.5a1 1 0 0 1 1 1c0 1.25.2 2.45.57 3.57a1 1 0 0 1-.25 1z"/></svg>9035550147</li>
    <li><svg viewBox="0 0 24 24"><path fill="currentColor" d="M12 2a7 7 0 0 0-7 7c0 5.2 7 13 7 13s7-7.8 7-13a7 7 0 0 0-7-7zm0 9.5A2.5 2.5 0 1 1 12 6.5a2.5 2.5 0 0 1 0 5z"/></svg>1840 Juniper Blvd<br>Wills Point, TX 75169</li>
    <li><svg viewBox="0 0 24 24"><path fill="currentColor" d="M3 5h18v14H3zm2 2v.5l7 4.5 7-4.5V7z"/></svg>basinslab@mailbox.net</li>
    <li><svg viewBox="0 0 24 24"><circle cx="12" cy="12" r="9" fill="none" stroke="currentColor" stroke-width="2"/><path d="M3 12h18M12 3c3 3 3 15 0 18M12 3c-3 3-3 15 0 18" fill="none" stroke="currentColor" stroke-width="1.6"/></svg>www.basinandslabinc.com</li>
  </ul>
</section>

<section class="card back" aria-label="Postcard back">
  <svg class="art" viewBox="0 0 696 530" aria-hidden="true">
    <path d="M0 0 H330 V90 C250 150 120 170 0 160 Z" fill="var(--charcoal)"/>
    <path d="M0 160 C120 170 250 150 330 90 V112 C250 172 120 192 0 184 Z" fill="var(--sky)"/>
    <path d="M0 515 C100 500 220 505 330 482 V530 H0 Z" fill="var(--sky)"/>
    <path d="M0 524 C110 510 230 514 330 494 V500 C230 520 110 518 0 530 Z" fill="var(--ice)"/>
  </svg>
  <div class="abs round-photo" role="img" aria-label="Round photo of a finished bathroom with cultured marble vanity"></div>
  <div class="abs about-title">ABOUT US</div>
  <div class="abs about-text">
    <p>Basin And Slab Inc. Has been providing the finest quality cultured marble products to the East Texas and Dallas area for over Thirty years. Scrubbing and wiping shower tile and grout lines is a hassle and time consuming. No matter how good it looks when you install it, tile leads to maintenance headaches down the road.</p>
    <p>Cultured marble is longer-lasting than acrylic shower and bathtub surrounds with more color options</p>
  </div>
  <div class="abs call">Call us 9035550147</div>
  <ul class="abs contact">
    <li><svg viewBox="0 0 24 24"><path fill="var(--sky)" d="M12 2a7 7 0 0 0-7 7c0 5.2 7 13 7 13s7-7.8 7-13a7 7 0 0 0-7-7zm0 9.5A2.5 2.5 0 1 1 12 6.5a2.5 2.5 0 0 1 0 5z"/></svg>1840 Juniper Blvd Wills Point,<br>TX 75169</li>
    <li><svg viewBox="0 0 24 24"><path fill="var(--sky)" d="M3 5h18v14H3zm2 2v.5l7 4.5 7-4.5V7z"/></svg>basinslab@mailbox.net</li>
    <li><svg viewBox="0 0 24 24"><circle cx="12" cy="12" r="9" fill="none" stroke="var(--sky)" stroke-width="2"/><path d="M3 12h18M12 3c3 3 3 15 0 18M12 3c-3 3-3 15 0 18" fill="none" stroke="var(--sky)" stroke-width="1.6"/></svg>www.basinandslabinc.com</li>
  </ul>
  <div class="abs stamp"></div>
</section>

</body>
</html>
```